Spiritual journeyer, astrologer, Reiki master, underground music lover needs business card design

Initially I need a business card design (and possibly a logo for my new website). I offer astrological and energetic inquiry and guidance to clients in support of their life's evolutionary path. I combine an eclectic mix of methods with a focus on the mind body connection. I am a spiritual journeyer, astrologer, Reiki Master, certified personal trainer, soon to be black belt in Taekwondo (karate), and researcher into the benefits of music/sound vibrational therapy. And underground music lover :) The attached drawing is just something I drew freehand, it is symbolic of many things important to me. I wanted the figure to clearly be female. Her arms are open to catch the sky, the name of my new business is Orlabrook, and Orla is my daughter's name. This was just an idea I had, I'm open to suggestions. The photo is me with the planets in the sky as they were at the moment I was born (some years ago-LOL)
Updates

I have picked a final design. Thank you everyone for your time and effort.

Target Market(s)

Worldwide, what I do can be done in person or anywhere in the world via Skype

Industry/Entity Type

Professional Service

Contact Information for Business Card

Simple, unusual image with my business name and contact info

Font styles to use
Sans Serif

Requirements
Must have
• My website very clean, simple. Somehow combine biz name of Orlabrook with female figure catching/holding the starry sky? See my poor drawing I attached.
Nice to have
• Something that conveys all the unique, unusual, eclectic skills and capacities I have
Should not have
• Frilly, fancy, stuffy

```html
<!DOCTYPE html>
<html lang="en">
<head>
<meta charset="utf-8">
<title>Orlabrook — Business Card</title>
<link rel="stylesheet" href="https://fonts.googleapis.com/css2?family=Open+Sans:wght@400;600&display=swap">
<style>
  :root {
    --backdrop: #141414;
    --card-white: #ffffff;
    --amber: #e08a0c;
    --amber-light: #f3b414;
    --amber-deep: #c7760c;
    --ink: #1c1c1c;
    --rule: #dcdcdc;
    --ring: #666666;
  }
  * { margin: 0; padding: 0; box-sizing: border-box; }
  html, body { width: 1200px; height: 900px; overflow: hidden; }
  body {
    background: var(--backdrop);
    font-family: "Open Sans", Arial, sans-serif;
    position: relative;
  }
  .card {
    position: absolute;
    top: 306px;
    width: 440px;
    height: 271px;
    border-radius: 10px;
    overflow: hidden;
    box-shadow: 0 2px 6px rgba(0,0,0,0.5);
  }
  .card--front { left: 149px; background: var(--card-white); }
  .card--back {
    left: 608px;
    background: radial-gradient(ellipse 210px 150px at 50% 50%, var(--amber-light) 0%, #e39a10 55%, var(--amber-deep) 100%);
  }

  /* front */
  .brand-mark {
    position: absolute;
    left: 40px; top: 118px;
    width: 172px;
    display: flex; align-items: center; justify-content: center; gap: 8px;
  }
  .brand-mark__dot {
    width: 14px; height: 14px; border-radius: 50%;
    background: var(--amber);
  }
  .brand-mark__name {
    font-size: 22px; font-weight: 600; color: var(--amber);
  }
  .divider {
    position: absolute;
    left: 219px; top: 74px;
    width: 1px; height: 150px;
    background: linear-gradient(to bottom, transparent, var(--rule) 20%, var(--rule) 80%, transparent);
  }
  .holder {
    position: absolute;
    left: 242px; top: 76px;
  }
  .holder__name {
    font-size: 16px; font-weight: 600; color: var(--amber);
    line-height: 22px;
  }
  .holder__role {
    font-size: 12.5px; color: var(--ink);
    line-height: 19px; margin-top: 1px;
  }
  .contact {
    list-style: none;
    margin-top: 12px;
  }
  .contact__item {
    display: flex; align-items: center; gap: 7px;
    font-size: 12.5px; color: var(--ink);
    line-height: 18.5px;
  }
  .contact__icon { width: 10px; height: 10px; flex: none; }

  /* back */
  .back-mark {
    position: absolute;
    left: 0; top: 0; width: 100%; height: 100%;
    display: flex; flex-direction: column; align-items: center;
  }
  .back-mark__ring {
    margin-top: 56px;
    width: 110px; height: 110px; border-radius: 50%;
    border: 5px solid var(--card-white);
  }
  .back-mark__name {
    margin-top: 4px;
    font-size: 41px; font-weight: 600; color: var(--card-white);
    letter-spacing: 0.3px;
  }
</style>
</head>
<body>
  <section class="card card--front" aria-label="Business card front">
    <div class="brand-mark">
      <span class="brand-mark__dot"></span>
      <span class="brand-mark__name">Orlabrook</span>
    </div>
    <div class="divider"></div>
    <div class="holder">
      <p class="holder__name">Maren Tolliver</p>
      <p class="holder__role">Astrological and Energetic<br>Guidance and Inquiry</p>
      <ul class="contact">
        <li class="contact__item">
          <svg class="contact__icon" viewBox="0 0 10 10" aria-hidden="true"><path d="M2 0.8 L3.6 2.6 L2.8 3.8 Q4 6.2 6.2 7.2 L7.4 6.4 L9.2 8 L8 9.4 Q4.5 9.4 2.2 6.8 Q0.4 4.6 0.6 2 Z" fill="var(--amber)"/></svg>
          555-210-947
        </li>
        <li class="contact__item">
          <svg class="contact__icon" viewBox="0 0 10 10" aria-hidden="true"><rect x="0.5" y="2" width="9" height="6.5" fill="var(--amber)"/><path d="M0.8 2.4 L5 5.8 L9.2 2.4" stroke="#fff" stroke-width="0.9" fill="none"/></svg>
          info@orlabrook.com
        </li>
        <li class="contact__item">
          <svg class="contact__icon" viewBox="0 0 10 10" aria-hidden="true"><circle cx="5" cy="5" r="4.5" fill="var(--amber)"/><path d="M0.5 5 H9.5 M5 0.5 Q2.5 5 5 9.5 M5 0.5 Q7.5 5 5 9.5" stroke="#fff" stroke-width="0.7" fill="none"/></svg>
          www.orlabrook.com
        </li>
      </ul>
    </div>
  </section>

  <section class="card card--back" aria-label="Business card back">
    <div class="back-mark">
      <div class="back-mark__ring"></div>
      <p class="back-mark__name">Orlabrook</p>
    </div>
  </section>
</body>
</html>
```